Warranty Card Design for Mattress Brand

We would like to design a warranty card for our mattresses,
it consists of 2 pages in one card (front and back) to be neatly showing our warranty details/text , our logo , our website, address and telephone clearly.

Target Market(s)

household

Font styles to use
Serif
Script

Colors
3277b5
33a6d7
85cae6
0492cd
3176b5
0355a3
85abd2
cee9f5
85acd3

Requirements
Must have
• a nice warranty logo
Nice to have
• a nice warranty logo with a neat text and clear layout, colors have to be related to the logo

```html
<!DOCTYPE html>
<html lang="en">
<head>
<meta charset="utf-8">
<title>Slumberly Warranty Card</title>
<link href="https://fonts.googleapis.com/css2?family=Open+Sans:wght@400;600;700&display=swap" rel="stylesheet">
<style>
  :root {
    --stage: #946866;
    --navy: #0355a3;
    --ink: #1d57a0;
    --brand: #3176b5;
    --pale: #cee9f5;
    --sky: #85cae6;
    --soft: #85abd2;
    --card: #f4fafd;
  }
  * { margin: 0; padding: 0; box-sizing: border-box; }
  html, body { width: 1200px; height: 1200px; overflow: hidden; }
  body {
    background: var(--stage);
    font-family: "Open Sans", Arial, sans-serif;
    color: var(--ink);
    position: relative;
  }
  .card {
    position: absolute;
    left: 154px;
    width: 892px;
    height: 401px;
    background: linear-gradient(100deg, var(--pale) 0%, var(--card) 45%, #ffffff 70%, var(--card) 100%);
    overflow: hidden;
  }
  .card--front { top: 204px; }
  .card--back { top: 642px; }
  .card__waves { position: absolute; inset: 0; width: 100%; height: 100%; }
  .card__content { position: absolute; inset: 0; }
  .abs { position: absolute; white-space: nowrap; }

  .front__title { left: 82px; top: 34px; font-size: 17px; font-weight: 400; color: var(--navy); }
  .front__intro { left: 25px; top: 66px; font-size: 11.3px; line-height: 15.5px; }
  .care-list { left: 25px; top: 158px; font-size: 11.3px; line-height: 15.8px; }
  .care-list ul { list-style: none; }
  .care-list li { position: relative; padding-left: 45px; }
  .care-list li::before { content: "•"; position: absolute; left: 2px; }
  .field { top: 268px; font-size: 11.3px; }
  .field--invoice { left: 309px; }
  .field--period { left: 536px; }
  .field--date { left: 762px; }

  .brand-name { font-size: 40px; font-weight: 400; color: var(--brand); letter-spacing: 0.5px; line-height: 1; }
  .brand-tag { font-size: 8px; letter-spacing: 2.2px; color: var(--brand); }
  .front__brand { left: 41px; top: 318px; }
  .front__tag { left: 56px; top: 370px; }

  .contact { font-size: 11.3px; line-height: 15.5px; font-style: normal; }
  .contact__name { font-weight: 700; color: var(--navy); }
  .front__contact { right: 27px; top: 320px; text-align: right; }

  .back__heading { left: 69px; font-size: 16.6px; font-weight: 700; color: var(--navy); }
  .back__heading--covers { top: 38px; }
  .back__heading--excludes { top: 120px; }
  .warranty-list { list-style: none; left: 39px; font-size: 11.3px; }
  .warranty-list li { position: relative; padding-left: 33px; }
  .warranty-list li::before { content: "•"; position: absolute; left: 0; }
  .warranty-list--covers { top: 66px; line-height: 21.5px; }
  .warranty-list .tight { letter-spacing: -0.45px; font-size: 11px; }
  .warranty-list--excludes { top: 159px; line-height: 21.2px; }
  .warranty-list .wrap { line-height: 14px; padding-bottom: 7px; padding-top: 2px; }
  .warranty-list .wrap span { display: block; padding-left: 21px; }

  .seal { position: absolute; left: 636px; top: 152px; width: 220px; height: 220px; border-radius: 50%;
    background: radial-gradient(circle, rgba(206,233,245,0.9) 0%, rgba(206,233,245,0.7) 70%, rgba(206,233,245,0.25) 100%); }
  .back__brand { left: 0; width: 100%; top: 32px; text-align: center; position: absolute; }
  .back__tag { left: 0; width: 100%; top: 84px; text-align: center; position: absolute; }
  .back__contact { left: 0; width: 100%; top: 112px; text-align: center; position: absolute; }
</style>
</head>
<body>

<section class="card card--front">
  <svg class="card__waves" viewBox="0 0 892 401" preserveAspectRatio="none" aria-hidden="true">
    <path d="M0 32 C 250 0 600 0 892 40 L892 0 L0 0 Z" fill="#cee9f5"/>
    <path d="M330 10 C 560 0 760 30 892 55 L892 62 C 760 40 560 12 330 10 Z" fill="#85cae6" opacity="0.7"/>
    <path d="M630 178 C 720 230 830 210 892 190 L892 125 C 850 140 790 150 730 165 C 700 172 665 178 630 178 Z" fill="#85cae6" opacity="0.6"/>
    <path d="M0 401 L0 270 C 120 240 260 250 420 320 C 520 362 600 370 660 358 C 620 390 560 401 520 401 Z" fill="#cee9f5"/>
    <path d="M360 300 C 480 370 590 370 548 360 C 500 352 430 330 360 300 Z" fill="#85abd2" opacity="0.7"/>
    <path d="M505 384 C 640 320 780 285 892 282 L892 301 C 780 298 650 335 505 384 Z" fill="#85abd2" opacity="0.8"/>
    <path d="M540 401 C 660 340 790 305 892 300 L892 401 Z" fill="#cee9f5"/>
  </svg>
  <div class="card__content">
    <h1 class="abs front__title">Congratulations on your new SLUMBERLY mattress.</h1>
    <p class="abs front__intro">
      We always strive to provide you with the most comfortable and healthy sleep by offering you the highest product quality and durability.<br>
      Our company was awarded the ISO 9001 accreditation certificate for the quality of its Mattress Production.<br>
      By implementing the ISO 9001 quality management system, we assure our customers that the products and the services we provide will meet their expectations.<br>
      Our products are guaranteed against defects in workmanship and material. In case of defect, we shall repair or replace, at our discretion, the defective component.<br>
      Pease keep this card in a safe place. Should you face any problems, please contact our service department
    </p>
    <div class="abs care-list">
      <p>To ensure you get maximum comfort and support, please follow the following instructions:</p>
      <ul>
        <li>Make sure the bed base foundation is in good condition and well ventilated.</li>
        <li>Turn/Flip your mattress every 3 months to maximize its comfort and lifespan.</li>
        <li>Avoid exposing the mattress to the sun; air it in a passage area instead.</li>
        <li>In case of possibility of liquids dripping on the mattress, consider covering it with a mattress protection pad.</li>
        <li>Do not worry if the mattress feels slightly firmer than anticipated within weeks of usage, the interior will soften and initial stiffness will be removed.</li>
      </ul>
    </div>
    <span class="abs field field--invoice">Invoice Number</span>
    <span class="abs field field--period">Warranty Period</span>
    <span class="abs field field--date">Date</span>

    <span class="abs brand-name front__brand">slumberly</span>
    <span class="abs brand-tag front__tag">mattresses &amp; Pillows</span>

    <address class="abs contact front__contact">
      <span class="contact__name">Haddad Rahme and Sons</span><br>
      Cedar Hill, Factory Lane, Metn, Lebanon<br>
      +961 1 555 010<br>
      www.haddadrahmeandsons.com
    </address>
  </div>
</section>

<section class="card card--back">
  <svg class="card__waves" viewBox="0 0 892 401" preserveAspectRatio="none" aria-hidden="true">
    <path d="M0 30 C 250 0 600 0 892 45 L892 0 L0 0 Z" fill="#cee9f5"/>
    <path d="M330 8 C 560 0 760 30 892 52 L892 60 C 760 38 560 12 330 8 Z" fill="#85cae6" opacity="0.7"/>
    <path d="M0 401 L0 330 C 80 320 200 325 280 360 C 230 385 170 401 140 401 Z" fill="#85cae6" opacity="0.55"/>
  </svg>
  <div class="card__content">
    <h2 class="abs back__heading back__heading--covers">This limited Mattress Warranty applies to the following Defects:</h2>
    <ul class="abs warranty-list warranty-list--covers">
      <li>Coils or wires that are broken or piercing through fabric.</li>
      <li class="tight">Sagging, that measures 3cm or greater (being properly measured) only if the mattress has been continuously supported by appropriate and solid foundation</li>
    </ul>
    <h2 class="abs back__heading back__heading--excludes">This limited Mattress Warranty does not cover the following:</h2>
    <ul class="abs warranty-list warranty-list--excludes">
      <li>Comfort preference</li>
      <li>Fabric Stains, soiling or burns</li>
      <li>Body impressions of less than 3cm</li>
      <li>Damage to the mattress due to abuse</li>
      <li>Bent Perimeter border rods due to moving or bending the mattress</li>
      <li>Size allowance of +/- 2cm</li>
      <li>Bed Bugs and Dust Mites</li>
      <li>Mattress Odor: as in any upholstery, new mattress may have odor that will fade with time</li>
      <li class="wrap">For Latex and Memory Foam mattresses: normal change in softness and recovery time in these<span>materials with time. This does not affect the relieving qualities of these mattresses.</span></li>
      <li>Transportation and Inspection Costs</li>
    </ul>

    <div class="seal" role="img" aria-label="Soft circular backdrop behind the brand name and contact details">
      <span class="brand-name back__brand">slumberly</span>
      <span class="brand-tag back__tag">mattresses &amp; Pillows</span>
      <address class="contact back__contact">
        <span class="contact__name">Haddad Rahme and Sons</span><br>
        Cedar Hill, Factory Lane, Metn, Lebanon<br>
        +961 1 555 010<br>
        www.haddadrahmeandsons.com
      </address>
    </div>
  </div>
</section>

</body>
</html>
```